Structural Engineering Company needs ad for magazine

We are an engineering office for structural engineering in the entertainment industry. Our focus are concert stages, festival structures, grand stands and exhibition booths. Our customers are mainly from Europe, we realize the projects worldwide. Typical customers are designer, architects, stage builders, exhibition builder and technical service provider. We are creating structural analyses, technical consulting, technical drawings and risk assessment. We are working on mid size and major events.
Some technical notes:
- CMYK profile needed, minimum 300 dpi for raster graphic
- Our primary color is Petrol. Favourite is petrol, coral and grey (black). Please use palette shown below.
- Our font in documents is Myriad. Regular at 10 pt for text and Light at 16-24pt for titles.
- The format for the ad is 61 x 127 mm (portrait) or 185 x 46 mm (landscape). Which one is up to you.
To the content:
- For contact details we just want to provide our web address "belsokar.de" and/or our e-mail "info@belsokar.de"
- Attached are some Logo files and photos.
- The ad do not advertise a specific product. It is more a general advertisement for the company.
- The language for the ad should be German. Below are keywords in English and corresponding German translation. You do not need to place all Keywords, it is just a brainstorming list to help you. You are also welcome to use other text. We will help with translation, if necessary.
- we like discussing ideas to get better results, so also if you have questions, please ask.
- If you need information that we haven't thought of yet, please ask.
Our slogan (also in Germany): event meets engineering
Service Keywords EN / DE
- Structural Analysis / Statische Berechnungen
- Risk Assessment / Risikobewertungen
- Consulting & Design / Beratung & Konstruktion
Technical Keywords EN / DE
- Stage machinery / Bühnentechnik
- Scaffolding / Gerüstbau
- Exhibition Booths / Messebauten
- Tents / Zelte
- Temporary Structures / Fliegende Bauten
- Truss / Traversen
- Stages / Bühnen
- Grand Stands / Tribünen
- Leightweight Construction / Leichtbau
- Steel Construction / Stahlbau
- Amusement Rides / Fahrgeschäfte
Look and feel
Each slider illustrates characteristics of the customer's brand and the style your logo design should communicate.

```html
<!DOCTYPE html>
<html lang="de">
<head>
<meta charset="utf-8">
<title>Belsokar Engineering – Anzeige</title>
<link href="https://fonts.googleapis.com/css2?family=Montserrat:wght@300;400;500;600&display=swap" rel="stylesheet">
<style>
  :root {
    --frame: #2aa9c4;
    --text: #ffffff;
    --text-soft: rgba(255,255,255,0.88);
    --steel: #9fb9c0;
    --teal-deep: #1d5a68;
    --teal-mid: #2f7f8e;
    --blue: #2e4fa0;
    --violet: #5b2aa3;
    --magenta: #9c38b6;
    --pink: #d676cc;
    --cyan-glow: #3fb8e6;
    --lilac: #c9a6e6;
  }
  html, body {
    margin: 0;
    padding: 0;
    width: 1200px;
    height: 2500px;
    overflow: hidden;
    background: #ffffff;
  }
  .ad {
    position: relative;
    width: 1200px;
    height: 2500px;
    box-sizing: border-box;
    border: 16px solid var(--frame);
    overflow: hidden;
    font-family: "Montserrat", Arial, sans-serif;
    color: var(--text);
    text-align: center;
  }
  .ad__backdrop {
    position: absolute;
    inset: 0;
    background:
      radial-gradient(ellipse 260px 700px at 88% 520px, rgba(190,210,215,0.55), transparent 70%),
      radial-gradient(ellipse 420px 260px at 40% 140px, rgba(170,195,205,0.45), transparent 70%),
      radial-gradient(ellipse 240px 420px at 12% 1200px, rgba(20,25,45,0.55), transparent 70%),
      radial-gradient(ellipse 560px 160px at 62% 1300px, rgba(215,175,235,0.6), transparent 70%),
      radial-gradient(ellipse 160px 240px at 68% 1500px, rgba(230,215,240,0.45), transparent 70%),
      radial-gradient(ellipse 220px 180px at 25% 1500px, rgba(235,150,225,0.55), transparent 70%),
      radial-gradient(ellipse 360px 260px at 82% 1980px, rgba(63,184,230,0.7), transparent 70%),
      radial-gradient(ellipse 300px 420px at 18% 1820px, rgba(214,118,204,0.55), transparent 70%),
      radial-gradient(ellipse 320px 220px at 30% 2380px, rgba(214,118,204,0.6), transparent 70%),
      radial-gradient(ellipse 300px 260px at 60% 1080px, rgba(40,30,80,0.45), transparent 70%),
      linear-gradient(180deg,
        var(--teal-mid) 0%,
        var(--teal-deep) 20%,
        #2a6f86 34%,
        #3a5aa8 46%,
        var(--violet) 62%,
        #6a2fae 74%,
        var(--magenta) 88%,
        var(--violet) 100%);
  }
  .ad__headline {
    position: absolute;
    top: 64px;
    left: 0;
    right: 0;
    margin: 0;
    font-weight: 600;
    font-size: 120px;
    line-height: 156px;
  }
  .ad__services {
    position: absolute;
    top: 658px;
    left: 0;
    right: 0;
    margin: 0;
    font-weight: 600;
    font-size: 86px;
    line-height: 106px;
  }
  .ad__mark {
    position: absolute;
    top: 1955px;
    left: 50%;
    width: 150px;
    height: 150px;
    margin-left: -75px;
  }
  .ad__brand {
    position: absolute;
    top: 2185px;
    left: 0;
    right: 0;
    margin: 0;
    font-weight: 500;
    font-size: 96px;
    line-height: 104px;
    letter-spacing: 0.2em;
    padding-left: 0.2em;
  }
  .ad__brand-sub {
    position: absolute;
    top: 2293px;
    left: 0;
    right: 0;
    margin: 0;
    font-weight: 300;
    font-size: 46px;
    line-height: 56px;
    letter-spacing: 0.24em;
    padding-left: 0.24em;
  }
  .ad__web {
    position: absolute;
    top: 2392px;
    left: 0;
    right: 0;
    margin: 0;
    font-weight: 400;
    font-size: 44px;
    line-height: 56px;
    color: var(--text-soft);
  }
</style>
</head>
<body>
  <div class="ad">
    <div class="ad__backdrop" role="img" aria-label="Unscharfes Veranstaltungsfoto: helle Traversenrohre oben, darunter Bühne mit blauem, violettem und pinkem Licht und Publikum"></div>
    <h1 class="ad__headline">Where event<br>meets<br>engineering.</h1>
    <p class="ad__services">Fachplanungsbüro für<br>Fliegende Bauten,<br>Messebau, Theater und<br>Veranstaltungstechnik.</p>
    <svg class="ad__mark" viewBox="0 0 150 150" aria-hidden="true">
      <circle cx="75" cy="75" r="64" fill="none" stroke="#ffffff" stroke-width="10"/>
    </svg>
    <p class="ad__brand">BELSOKAR</p>
    <p class="ad__brand-sub">ENGINEERING</p>
    <p class="ad__web">www.belsokar.de</p>
  </div>
</body>
</html>
```